Black card, Logo on front, in brushed silver, embossed or stamped
details centred on the back of the card written in Serif Old type face
Hotel
Amber Heron Hotel Motel (or smaller logo)
your hosts
Colin and Marisa Doyle
left bottom:
7 Harcourt Street
Kestrel Vale NSW 2719
right bottom:
P: 02 61739485
M: 0428 315 947
W: www.amberheronhotel.com.au
E: amberheronhotel@mailbox.example
facebook emblem: @AmberHeronHotel
instagram emblem: @amberheronhotel

```html
<!DOCTYPE html>
<html lang="en">
<head>
<meta charset="utf-8">
<title>Amber Heron Hotel Motel – Business Card</title>
<link rel="stylesheet" href="https://fonts.googleapis.com/css2?family=Old+Standard+TT:wght@400&display=swap">
<style>
  :root {
    --backdrop: #4a3f3a;
    --card: #1c1c1d;
    --card-edge: #111112;
    --silver: #b9babd;
    --silver-soft: #9c9da1;
  }
  * { box-sizing: border-box; margin: 0; padding: 0; }
  html, body { width: 1200px; height: 716px; overflow: hidden; }
  body {
    background: var(--backdrop);
    font-family: "Old Standard TT", Georgia, serif;
    color: var(--silver);
    display: flex;
    align-items: center;
    justify-content: center;
    gap: 60px;
  }
  .card {
    width: 520px;
    height: 318px;
    background: var(--card);
    border: 1px solid var(--card-edge);
    box-shadow: 0 14px 30px rgba(0,0,0,0.45);
    position: relative;
  }
  .brand {
    display: flex;
    align-items: center;
    justify-content: center;
    gap: 12px;
    color: var(--silver);
    text-transform: uppercase;
    letter-spacing: 0.14em;
  }
  .brand-dot {
    border-radius: 50%;
    background: var(--silver);
    flex: none;
  }
  .card--front .brand {
    position: absolute;
    inset: 0;
    font-size: 22px;
  }
  .card--front .brand-dot { width: 16px; height: 16px; }

  .card--back .brand {
    position: absolute;
    top: 48px;
    left: 0;
    right: 0;
    font-size: 17px;
  }
  .card--back .brand-dot { width: 12px; height: 12px; }
  .hosts {
    position: absolute;
    top: 106px;
    left: 0;
    right: 0;
    text-align: center;
    font-size: 16px;
    color: var(--silver);
  }
  .details {
    position: absolute;
    bottom: 34px;
    font-size: 13px;
    line-height: 1.55;
    color: var(--silver-soft);
    list-style: none;
  }
  .details--address { left: 36px; }
  .details--contact { right: 30px; }
  .details li { display: flex; align-items: center; gap: 7px; white-space: nowrap; }
  .icon { width: 11px; height: 11px; flex: none; }
  .social-mark {
    width: 10px; height: 10px; flex: none;
    background: var(--silver-soft);
    border-radius: 2px;
  }
</style>
</head>
<body>
  <section class="card card--front" aria-label="Card front">
    <div class="brand"><span class="brand-dot"></span><span class="brand-name">Amber Heron Hotel Motel</span></div>
  </section>

  <section class="card card--back" aria-label="Card back">
    <div class="brand"><span class="brand-dot"></span><span class="brand-name">Amber Heron Hotel Motel</span></div>
    <p class="hosts">Colin and Marisa Doyle</p>

    <ul class="details details--address">
      <li>7 Harcourt Street</li>
      <li>Kestrel Vale NSW 2719</li>
      <li><span class="social-mark"></span>@AmberHeronHotel</li>
      <li><span class="social-mark"></span>@amberheronhotel</li>
    </ul>

    <ul class="details details--contact">
      <li>
        <svg class="icon" viewBox="0 0 12 12" aria-hidden="true"><path d="M3 1l2 2.5-1.2 1.3a6 6 0 0 0 3.4 3.4L8.5 7 11 9l-1.5 2C5 11 1 7 1 2.5z" fill="var(--silver-soft)"/></svg>
        02 61739485
      </li>
      <li>
        <svg class="icon" viewBox="0 0 12 12" aria-hidden="true"><rect x="3" y="0.8" width="6" height="10.4" rx="1" fill="none" stroke="var(--silver-soft)" stroke-width="1.2"/><circle cx="6" cy="9.3" r="0.7" fill="var(--silver-soft)"/></svg>
        0428 315 947
      </li>
      <li>
        <svg class="icon" viewBox="0 0 12 12" aria-hidden="true"><g fill="none" stroke="var(--silver-soft)" stroke-width="1"><circle cx="6" cy="6" r="5"/><ellipse cx="6" cy="6" rx="2.2" ry="5"/><line x1="1" y1="6" x2="11" y2="6"/></g></svg>
        www.amberheronhotel.com.au
      </li>
      <li>
        <svg class="icon" viewBox="0 0 12 12" aria-hidden="true"><rect x="0.8" y="2.3" width="10.4" height="7.4" fill="none" stroke="var(--silver-soft)" stroke-width="1.1"/><path d="M1 2.6l5 4 5-4" fill="none" stroke="var(--silver-soft)" stroke-width="1.1"/></svg>
        amberheronhotel@mailbox.example
      </li>
    </ul>
  </section>
</body>
</html>
```